New Business Card for Software Company

We are looking at rebranding a 10 year old company that specializes in PDF and DWF solutions for Architects and Engineers. We will attach the new company logo that we are going with so you can work with that and complimentary colors.
The sample information we would like on the business card is:
Gerald Pembrook
Vice President
4173 W. Tillman Avenue. STE 306
PMB#417
Mesa, AZ 85316
866-392-7154 US Toll Free
123-581-3064 Cell
gpembrook@vextrolan.com
The old tag line that we had on the business cars was.
Providing Industrial Strength PDF and DWF Solutions to the Global CAD Marketplace.
If you have an idea for a better tag line we are open to that also.
Updates
We would like to thank all of the Designers for their wonderful work. We apologize that we will not have the time to provide feedback to everyone. There is just so many innovative and professional designs that you have all created making our decision even harder.
Target Market(s)
Architects and Engineers
Industry/Entity Type
Business
Look and feel
Each slider illustrates characteristics of the customer's brand and the style your logo design should communicate.

```html
<!DOCTYPE html>
<html lang="en">
<head>
<meta charset="utf-8">
<title>Vextrolan Business Card</title>
<link rel="stylesheet" href="https://fonts.googleapis.com/css2?family=Source+Sans+3:ital,wght@0,600;0,700;1,700&display=swap">
<style>
  :root {
    --stage-edge: #d4e8b5;
    --stage-mid: #8cc63f;
    --orange-deep: #f15a29;
    --orange-warm: #f7941d;
    --orange-pale: #fde3c6;
    --paper: #ffffff;
    --ink: #1a1a1a;
    --brand: #f26522;
  }
  * { margin: 0; padding: 0; box-sizing: border-box; }
  html, body { width: 1200px; height: 914px; overflow: hidden; }
  body {
    position: relative;
    background: linear-gradient(90deg, var(--stage-edge) 0%, var(--stage-mid) 50%, var(--stage-edge) 100%);
    font-family: "Source Sans 3", "Myriad Pro", Arial, sans-serif;
    color: var(--ink);
  }
  .card { position: absolute; overflow: hidden; background: var(--paper); }
  .card-front { left: 97px; top: 51px; width: 662px; height: 377px; }
  .card-back { left: 439px; top: 482px; width: 661px; height: 378px; }

  .card-backdrop {
    position: absolute; inset: 0;
    background: linear-gradient(90deg,
      var(--orange-deep) 0%,
      var(--orange-warm) 7%,
      var(--orange-pale) 15%,
      var(--paper) 24%,
      var(--paper) 76%,
      var(--orange-pale) 85%,
      var(--orange-warm) 93%,
      var(--orange-deep) 100%);
  }

  .brand { position: absolute; display: flex; align-items: center; color: var(--brand); font-weight: 700; letter-spacing: -0.5px; }
  .brand-dot { border-radius: 50%; background: var(--brand); }
  .card-front .brand { left: 190px; top: 78px; font-size: 38px; gap: 12px; }
  .card-front .brand-dot { width: 42px; height: 42px; }
  .card-back .brand { left: 100px; top: 38px; font-size: 64px; gap: 16px; }
  .card-back .brand-dot { width: 78px; height: 78px; }

  .person { position: absolute; left: 92px; top: 236px; font-style: italic; font-weight: 700; font-size: 19px; line-height: 24px; }
  .divider { position: absolute; left: 287px; top: 196px; width: 2px; height: 140px;
    background: linear-gradient(180deg, rgba(241,90,41,0) 0%, var(--orange-deep) 50%, rgba(241,90,41,0) 100%); }
  .contact { position: absolute; left: 330px; top: 200px; font-style: normal; font-weight: 700; font-size: 16px; line-height: 21px; }

  .tagline { position: absolute; font-style: italic; font-weight: 700; font-size: 15.5px; line-height: 26px; }
  .tagline-one { left: 102px; top: 136px; }
  .tagline-two { left: 213px; top: 162px; }
</style>
</head>
<body>

<section class="card card-front" aria-label="Business card front">
  <div class="card-backdrop" role="img" aria-label="Decorative orange curtain sweep framing the card edges"></div>

  <div class="brand"><span class="brand-dot"></span>Vextrolan</div>

  <p class="person">Gerald Pembrook<br>Vice President</p>
  <span class="divider"></span>
  <address class="contact">
    4173 W. Tillman Avenue. STE 306<br>
    PMB#417<br>
    Mesa, AZ 85316<br>
    866-392-7154 US Toll Free<br>
    123-581-3064 Cell<br>
    gpembrook@vextrolan.com
  </address>
</section>

<section class="card card-back" aria-label="Business card back">
  <div class="card-backdrop" role="img" aria-label="Decorative orange curtain sweep framing the card edges"></div>

  <div class="brand"><span class="brand-dot"></span>Vextrolan</div>

  <p class="tagline tagline-one">Providing Industrial Strength PDF and DWF</p>
  <p class="tagline tagline-two">Solutions to the Global CAD Marketplace ..........</p>
</section>

</body>
</html>
```